Letterhead for Midwest Law Firm

Our law firm does estate planning and trust administration in Wisconsin and Illinois. We recently obtained a new logo and need to incorporate it into new stationary. The stationary needs to list out the attorneys at the firm, but we will want 3 variations, one with three attorneys, one with six, and one with six plus the names of states where each is licensed to practice (possibly as an asterisk with notation somewhere towards bottom of page. As with most traditional law practices, letterhead should be conservative and convey predictability and reliability. We view our brand as being primarily reliability, with prestige as a secondary element. We are upmarket, but would like to avoid seeming pretentious or "slick". We are a smaller firm with a personal touch.

Target Market(s)

Affluent Midwestern Americans approaching at or approaching retirement age.

Industry/Entity Type

Legal

Font styles to use
Serif
Sans Serif

Requirements
Must have
• Must use our logo. Must comply with Northgate Counsel Guild Ethics rules: https://www.quarvenlex.org/rules/offices/docs/plmtk41annotated.pdf. Must be conventional. Must list names of attorneys and provide contact information for firm. Note that we are asking for three designs with very minor variations. Also, designer must provide letterhead in a format that is industry-standard for stationary printers.
Nice to have
• We would appreciate an alternate version that will look reasonable when printed on a black-and-white printer. Designer can use judgment as to whether to have use grayscale, black/white, or something in between.
Should not have
• No "motto" or "visit our website" extraneous materials. putting the website address somewhere is fine, but overall there is a lot of required text, and we'd like to not appear cluttered.

```html
<!DOCTYPE html>
<html lang="en">
<head>
<meta charset="utf-8">
<title>Hallbrook &amp; Wren LLP — Letterhead</title>
<link rel="stylesheet" href="https://fonts.googleapis.com/css2?family=Libre+Baskerville:wght@700&family=Roboto+Slab:wght@400;500&family=Poppins:wght@400;500;600&family=Comfortaa:wght@500&display=swap">
<style>
  :root {
    --navy: #2b2a3f;
    --gold: #f2ae2a;
    --blue: #14a3dc;
    --ink: #2c2c2c;
    --muted: #8a8a8a;
    --orange: #f0883a;
    --rule: #d6d6d6;
    --backdrop: #cdcdcf;
    --paper: #ffffff;
  }
  * { box-sizing: border-box; margin: 0; padding: 0; }
  html, body { width: 1200px; height: 1200px; overflow: hidden; }
  body { background: var(--backdrop); font-family: "Poppins", sans-serif; color: var(--ink); }

  .sheet {
    position: absolute; left: 250px; top: 107px;
    width: 701px; height: 987px;
    background: var(--paper);
    overflow: hidden;
  }
  .abs { position: absolute; }

  .firm-mark { left: 0; right: 0; top: 72px; display: flex; justify-content: center; align-items: center; gap: 12px; }
  .firm-mark__dot { width: 18px; height: 18px; border-radius: 50%; background: var(--gold); }
  .firm-mark__name { font-family: "Libre Baskerville", serif; font-weight: 700; font-size: 24px; color: var(--navy); }

  .divider { left: 0; top: 170px; width: 701px; height: 14px; }

  .recipient { left: 40px; top: 216px; }
  .recipient__to { font-size: 10px; }
  .recipient__name { font-family: "Roboto Slab", serif; font-weight: 500; font-size: 14px; color: var(--orange); margin-top: 1px; }
  .recipient__role { font-family: "Roboto Slab", serif; font-size: 11px; color: var(--muted); margin-top: 1px; }
  .recipient__web { font-size: 10.5px; margin-top: 4px; }

  .letter-date { right: 46px; top: 264px; font-size: 10.5px; }
  .letter-date span { color: var(--gold); }

  .letter-body { left: 40px; top: 354px; width: 615px; font-size: 10.6px; line-height: 16.2px; }
  .letter-body p { margin-bottom: 16px; }
  .letter-body .is-muted { color: var(--muted); }

  .signature { left: 46px; top: 748px; width: 152px; height: 38px; background: linear-gradient(90deg, #eeeef2, #e4e4ea); border-radius: 3px; }
  .signature__line { left: 46px; top: 794px; width: 152px; height: 1.5px; background: var(--navy); }
  .signature__title { left: 64px; top: 806px; font-size: 9.5px; font-weight: 500; color: var(--navy); }

  .faint-mark { right: 26px; top: 760px; font-family: "Libre Baskerville", serif; font-weight: 700; font-size: 30px; color: #f1f1f3; text-align: right; line-height: 1.2; }

  .footer-rule { left: 18px; top: 863px; width: 672px; height: 1px; background: var(--rule); }
  .contacts { top: 888px; font-family: "Comfortaa", sans-serif; font-weight: 500; font-size: 10.5px; line-height: 17px; color: var(--ink); }
  .contacts li { list-style: none; display: flex; align-items: center; gap: 6px; }
  .contacts svg { width: 10px; height: 10px; flex: none; }
  .contacts--phone { left: 30px; }
  .contacts--web { left: 226px; }
  .contacts--address { left: 472px; }

  .attorney-band { left: 0; top: 943px; width: 701px; height: 44px; background: var(--navy); }
  .attorney-band__tab { position: absolute; left: 0; top: 0; width: 210px; height: 44px; }
  .attorney-band__label { position: absolute; left: 50px; top: 11px; font-size: 16px; font-weight: 600; color: #fff; letter-spacing: 0.3px; }
  .attorney-band__names { position: absolute; left: 233px; top: 14px; font-size: 11.5px; font-weight: 500; color: var(--gold); }
</style>
</head>
<body>
  <main class="sheet">
    <header class="firm-mark abs">
      <span class="firm-mark__dot"></span>
      <span class="firm-mark__name">Hallbrook &amp; Wren LLP</span>
    </header>

    <svg class="divider abs" viewBox="0 0 701 14" aria-hidden="true">
      <rect x="0" y="5.5" width="701" height="3" fill="var(--blue)"/>
      <rect x="234" y="0.5" width="13" height="13" fill="var(--navy)"/>
      <rect x="251" y="0.5" width="198" height="13" fill="var(--gold)"/>
      <rect x="453" y="0.5" width="13" height="13" fill="var(--navy)"/>
    </svg>

    <section class="recipient abs">
      <p class="recipient__to">To</p>
      <p class="recipient__name">Dana Whitlow</p>
      <p class="recipient__role">CEO, FERNLIGHT STUDIO</p>
      <p class="recipient__web">website: www.fernlightstudio.com</p>
    </section>
    <p class="letter-date abs"><span>Date:</span> 24-03-2018</p>

    <article class="letter-body abs">
      <p>Lorem ipsum dolor sit amet, consectetur adipiscing elit. Pellentesque dictum, ante non ullamcorp er convallis, nunc quam blandit metus, ac mollis eros felis a orci. Donec congue, mauris ut pulvinar lobortis, dolor massa feugiat nisi, at tincidunt metus leo vel elit. Proin facilisis semper lobortis. Vivamus augue purus, cursus quis urna non, accumsan pellen­tesque est. Nulla in iaculis magna, quis aliqu et ex. Cras efficitur metus eget purus euismod facilisis. Proin non metus tincidunt, auctor ipsum a, tempor mi.</p>
      <p class="is-muted">Nulla egestas vulputate risus, ut vestibulum diam commodo id. Mauris ornare libero eu erat portt itor ultrices. Proin sed lectus scelerisque ligula bibendum sagittis ac nec leo. Donec ac accumsan diam, et lobortis mauris.</p>
      <p class="is-muted">Nulla congue volutpat nisl ac lobortis. Integer dignissim interdum libero, quis feugiat velit pretium at. Phasellus sit amet libero rutrum, feugiat odio et, tempus purus. Cras ultricies, leo at fringilla solli cit udin, leo sapien placerat enim, a rutrum lorem enim ut tortor. Phasellus magna ante, cong ue maximus egestas sit amet, venenatis scelerisque felis.</p>
      <p>Nulla congue volutpat nisl ac lobortis. Integer dignissim interdum libero, quis feugiat velit pretium at. Phasellus sit amet libero rutrum, feugiat odio et, tempus purus. Cras ultricies, leo at fringilla solli cit udin, leo sapien placerat enim, a rutrum lorem enim ut tortor. Phasellus magna ante, cong ue maximus egestas sit amet, venenatis scelerisque felis.</p>
      <p>Curabitur vitae urna volutpat, varius velit vehicula, fermentum magna. In maximus metus nunc, nec aliquet justo com­modo eget. Nullam rhoncus vehicula gravida. Maecenas non sem at erat lacinia con vallis. Aliquam at lobortis erat.</p>
    </article>

    <div class="signature abs" role="img" aria-label="Handwritten signature of the signing attorney"></div>
    <div class="signature__line abs"></div>
    <p class="signature__title abs">DESIGNATION PLACE HERE</p>

    <p class="faint-mark abs" aria-hidden="true">Hallbrook<br>&amp; Wren</p>

    <div class="footer-rule abs"></div>
    <ul class="contacts contacts--phone abs">
      <li><svg viewBox="0 0 10 10"><path d="M2 0.5 L3.8 2.6 L2.9 3.7 Q4 6 6.3 7.1 L7.4 6.2 L9.5 8 L8.4 9.5 Q3.5 9 0.5 1.6 Z" fill="var(--orange)"/></svg>555-014-7200</li>
      <li><svg viewBox="0 0 10 10"><rect x="0.8" y="2" width="8.4" height="7.5" fill="none" stroke="var(--orange)" stroke-width="1.2"/><rect x="2.5" y="0.5" width="5" height="3" fill="var(--orange)"/><rect x="2.5" y="5" width="5" height="1" fill="var(--orange)"/><rect x="2.5" y="7" width="5" height="1" fill="var(--orange)"/></svg>555-014-0664</li>
    </ul>
    <ul class="contacts contacts--web abs">
      <li><svg viewBox="0 0 10 10"><rect x="0.8" y="2" width="8.4" height="6" fill="none" stroke="var(--orange)" stroke-width="1.1"/><path d="M1 2.3 L5 5.3 L9 2.3" fill="none" stroke="var(--orange)" stroke-width="1.1"/></svg>info@hallbrookwrenllp.com</li>
      <li><svg viewBox="0 0 10 10"><circle cx="5" cy="5" r="4.2" fill="none" stroke="var(--orange)" stroke-width="1.1"/><ellipse cx="5" cy="5" rx="1.8" ry="4.2" fill="none" stroke="var(--orange)" stroke-width="0.9"/><path d="M0.8 5 H9.2" stroke="var(--orange)" stroke-width="0.9"/></svg>www.hallbrookwrenllp.com</li>
    </ul>
    <ul class="contacts contacts--address abs">
      <li>218 East Linden Avenue, Suite 300,</li>
      <li>Ashford, Wisconsin 53990</li>
    </ul>

    <footer class="attorney-band abs">
      <svg class="attorney-band__tab" viewBox="0 0 210 44" aria-hidden="true"><polygon points="0,0 186,0 210,22 186,44 0,44" fill="var(--blue)"/></svg>
      <span class="attorney-band__label">ATTORNEYS</span>
      <span class="attorney-band__names">Thomas C. Hallbrook, Peter R Hallbrook, Gavin J Wren</span>
    </footer>
  </main>
</body>
</html>
```